Corporate Financial Services

This is a new Company. The ORV represents my son's and my own Christian name initials (ORV) (Colin and Neil) but no real significance.
This is a boutique financial services company active in the full parameter of corporate and business transactions. From standard financial and tax services to specialised Research & Development, mergers and acquisitions, business valuations, and capital raising.
Over 30 years of experience with listed and private entities.
I am after something exciting, given the nature of the business, bright, clean and colourful, but not in comic form.
Updates
Hi there,
Firstly thankyou for accepting the challenge. I have no ideas and nothing to compare your submissions with other than other peoples cards.
A few points
I omitted the ABN number from the card description. This is an important reference for all businesses operating in Australia. Therefore the following should be shown in association with the company name ORV Corporate & Financial Services Pty Ltd It can either be within brackets or without but always shown underneath the company name in smaller font.
The eight core business services need to be shown on the reverse
My contact number should also be shown along side the address
My business title is Chartered Accountant in full. I am also not fussed as to whether my name appears in caps or Caps and lowercase ie Neil Barrow or NEIL BARROW but this will depend upon the design of the rest of the card.
Maybe a small logo for the company needs to be attached but not sure.
Kind regards
Neil Barrow
Industry/Entity Type
Financial
Contact Information for Business Card
ORV Corporate & Financial Services Pty Ltd
(ABN 71 384 902 157)
(Note ABN could be shown on the reverse side with just ORV Corporate & Financial Services Pty Ltd on the front....no ABN
17 Wattlebank Road Wattlebank SA 5164
Neil Barrow
Chartered Accountant
Phone (symbol preferred) +61 (0) 437 215086
Email (symbol) to be provided
www.orv-example.com.au
Skype neil7312
Requirements
Must have
- On the reverse:
Corporate Finance
Taxation
Research & Development Specialisation
Financial Accounting
Mergers & Acquisitions
Company Listings (IPO's)
Business Valuations
Capital Raising
Nice to have
- Interested in a strong black card (or grey white platinum and black colours) with either platinum or gold highlight modern name style no italics. I would also like at a later stage with the winner to use this same design for card for Asia with a red and or gold and platinum colour. But I want this batch first.
The smart block (square) for digital image transfer to mobile phones contained within a gold or platinum square border on reverse of the card
Should not have
Anything old or staid looking. No italics sans serif

```html
<!DOCTYPE html>
<html lang="en">
<head>
<meta charset="utf-8">
<title>ORV Corporate &amp; Financial Services – Business Card</title>
<link rel="stylesheet" href="https://fonts.googleapis.com/css2?family=Cinzel:wght@500;600&family=Open+Sans:wght@400;600;700&display=swap">
<style>
  :root {
    --backdrop: #e8e6e2;
    --card-dark: #262728;
    --card-dark-edge: #1b1c1d;
    --card-light: #f7f7f5;
    --gold: #c9a227;
    --gold-light: #ecd27a;
    --gold-deep: #a27c12;
    --ink: #2a2a2a;
    --text-light: #eeeeee;
    --text-muted: #c8c8c8;
  }
  * { box-sizing: border-box; margin: 0; padding: 0; }
  html, body {
    width: 1200px; height: 800px; overflow: hidden;
    background: var(--backdrop);
    font-family: "Open Sans", Arial, sans-serif;
  }
  .canvas {
    position: relative; width: 1200px; height: 800px;
    display: flex; flex-direction: column; align-items: center; justify-content: center; gap: 40px;
  }
  .card {
    position: relative; width: 560px; height: 320px;
    border-radius: 16px; overflow: hidden;
    box-shadow: 0 6px 18px rgba(0,0,0,0.18);
  }
  .card-shapes { position: absolute; inset: 0; }

  /* Front */
  .front { background: var(--card-dark); }
  .brand { position: absolute; text-align: center; }
  .front .brand { left: 265px; top: 22px; width: 240px; }
  .brand-mark {
    font-family: "Open Sans", Arial, sans-serif; font-weight: 700;
    letter-spacing: 4px; line-height: 1;
  }
  .front .brand-mark { font-size: 52px; color: var(--ink); }
  .brand-name {
    font-family: "Cinzel", Georgia, serif; font-weight: 600;
    letter-spacing: 0.5px; white-space: nowrap;
  }
  .front .brand-name { font-size: 11.5px; color: var(--ink); margin-top: 6px; }

  .person { position: absolute; left: 30px; top: 92px; }
  .person-name { font-weight: 700; font-size: 17px; color: var(--gold); letter-spacing: 0.5px; }
  .person-title { font-size: 13px; color: var(--text-light); margin-top: 4px; }

  .abn {
    position: absolute; right: 18px; top: 252px;
    font-size: 10px; font-weight: 600; color: var(--ink);
    transform: rotate(23.2deg); transform-origin: right center;
  }

  .divider-vertical {
    position: absolute; left: 178px; top: 218px; width: 1px; height: 80px;
    background: linear-gradient(var(--gold-light), var(--gold-deep));
  }
  .contact-list { position: absolute; left: 198px; top: 224px; list-style: none; }
  .contact-list li {
    display: flex; align-items: center; gap: 8px;
    font-size: 12px; color: var(--text-light); height: 18px;
  }
  .contact-list svg { width: 13px; height: 13px; flex: none; }

  /* Back */
  .back { background: linear-gradient(135deg, #2d2e2f, var(--card-dark-edge)); }
  .back .brand { left: 0; right: 0; top: 70px; }
  .back .brand-mark { font-size: 64px; color: var(--gold); }
  .back .brand-name { font-size: 16px; color: var(--gold); margin-top: 10px; }
  .divider-horizontal {
    position: absolute; left: 24px; right: 24px; top: 204px; height: 1px;
    background: linear-gradient(90deg, transparent, var(--gold-light) 20%, var(--gold) 80%, transparent);
  }
  .service-list { position: absolute; top: 220px; list-style: none; }
  .service-list.first { left: 40px; }
  .service-list.second { left: 340px; }
  .service-list li {
    font-size: 11.5px; color: var(--text-muted); height: 19px;
    display: flex; align-items: center; gap: 8px;
  }
  .service-list li::before {
    content: ""; width: 5px; height: 5px; border-radius: 50%; background: var(--gold);
  }
</style>
</head>
<body>
<main class="canvas">

  <section class="card front" aria-label="Business card front">
    <svg class="card-shapes" viewBox="0 0 560 320" aria-hidden="true">
      <defs>
        <linearGradient id="goldBand" x1="0" y1="0" x2="1" y2="0">
          <stop offset="0" stop-color="#f3e3a4"/>
          <stop offset="0.5" stop-color="#d9b53e"/>
          <stop offset="1" stop-color="#c9a227"/>
        </linearGradient>
      </defs>
      <polygon points="0,0 560,0 560,270 0,30" fill="#f7f7f5"/>
      <polygon points="0,30 560,270 560,288 0,48" fill="url(#goldBand)"/>
    </svg>

    <div class="brand">
      <div class="brand-mark">ORV</div>
      <div class="brand-name">Corporate &amp; Financial Services Pty Ltd</div>
    </div>

    <div class="person">
      <div class="person-name">NEIL BARROW</div>
      <div class="person-title">Chartered Accountant</div>
    </div>

    <div class="abn">ABN 71 384 902 157</div>

    <div class="divider-vertical"></div>
    <ul class="contact-list">
      <li>
        <svg viewBox="0 0 14 14" aria-hidden="true"><circle cx="7" cy="7" r="7" fill="var(--gold)"/><path d="M4.6 3.6l1.3 1.5-.7 1c.5 1 1.2 1.7 2.2 2.2l1-.7 1.5 1.3-.8 1.2C6.7 10 4 7.3 3.8 4.4z" fill="#262728"/></svg>
        +61 (0) 437 215086
      </li>
      <li>
        <svg viewBox="0 0 14 14" aria-hidden="true"><circle cx="7" cy="7" r="7" fill="var(--gold)"/><rect x="3.5" y="4.5" width="7" height="5" fill="#262728"/><path d="M3.5 4.5L7 7.3l3.5-2.8" stroke="var(--gold)" stroke-width="0.8" fill="none"/></svg>
        neilbarrow@orv-example.com.au
      </li>
      <li>
        <svg viewBox="0 0 14 14" aria-hidden="true"><circle cx="7" cy="7" r="7" fill="var(--gold)"/></svg>
        neil7312
      </li>
      <li>
        <svg viewBox="0 0 14 14" aria-hidden="true"><circle cx="7" cy="7" r="7" fill="var(--gold)"/><g stroke="#262728" stroke-width="0.8" fill="none"><circle cx="7" cy="7" r="4"/><ellipse cx="7" cy="7" rx="1.8" ry="4"/><path d="M3 7h8"/></g></svg>
        www.orv-example.com.au
      </li>
    </ul>
  </section>

  <section class="card back" aria-label="Business card back">
    <div class="brand">
      <div class="brand-mark">ORV</div>
      <div class="brand-name">Corporate &amp; Financial Services Pty Ltd</div>
    </div>
    <div class="divider-horizontal"></div>
    <ul class="service-list first">
      <li>Corporate Finance</li>
      <li>Taxation</li>
      <li>Research &amp; Development Specialisation</li>
      <li>Financial Accounting</li>
    </ul>
    <ul class="service-list second">
      <li>Mergers &amp; Acquisitions</li>
      <li>Company Listings (IPO's)</li>
      <li>Business Valuations</li>
      <li>Capital Raising</li>
    </ul>
  </section>

</main>
</body>
</html>
```